QV Holdings Website Redesign Contest

We want to refresh our website to be more insitutional, professional for an international audience. We have designed a new logo for this purpose and that has been attached. A full brand brief and positioning statement has also been attached. Please read through all the documents carefully before designing. The old website is found here: https://qv-holdings.example/

Target Market(s)

Actuaries and associated businesses internationally

Industry/Entity Type

professional services - actuaries

Number of Pages Required

3 page

Font styles to use
Sans Serif

Colors
0054AA
0677BA
7BADD7
CADEEF
E8F1F8
0094D4
00A9DD
6FCCEA
C7EBF8
E9F6FB
F0912C
F2A743
F7CA91
FBE8D2
FDF5EE
EE7325
F08F49
F5BC92
FAE3D3
FDF4ED
EB3D1F
EC4F4E
F09395
F8D3D4
FCEDEE

Requirements
Must have
• blues and greens to match the logo color, complimentary colors, navigation
Nice to have
• old site: https://qv-holdings.example/

```html
<!DOCTYPE html>
<html lang="en">
<head>
<meta charset="utf-8">
<title>QV Holdings — Actuarial Software</title>
<link rel="stylesheet" href="https://fonts.googleapis.com/css2?family=Inter:wght@400;500;600;700;800&display=swap">
<style>
:root{
  --stage:#afadb0;
  --white:#ffffff;
  --ink:#0b0b0f;
  --muted:#4a4d55;
  --blue:#0052ff;
  --blue-deep:#0a2a8c;
  --blue-hero:#0d3fc4;
  --orange:#ff6f00;
  --soft:#f4f8fd;
  --line:#e3e7ee;
  --footer:#000000;
}
*{box-sizing:border-box;margin:0;padding:0}
html,body{width:1200px;height:2301px;overflow:hidden}
body{background:var(--stage);font-family:"Inter",Arial,sans-serif;color:var(--ink)}
.page{position:absolute;left:95px;top:95px;width:1011px;height:2110px;background:var(--white);box-shadow:0 6px 24px rgba(0,0,0,.18);overflow:hidden}

/* header */
.site-header{height:63px;display:flex;align-items:center;justify-content:space-between;padding:0 19px;border-bottom:1px solid #e6e9f0}
.brand{font-weight:700;font-size:21px;letter-spacing:1.5px;color:var(--blue-deep);display:flex;align-items:center;gap:8px}
.brand-dot{width:12px;height:12px;border-radius:50%;background:var(--orange)}
.main-nav{display:flex;align-items:center;gap:18px;font-size:12px;font-weight:500}
.btn{display:inline-block;font-weight:600;color:var(--white);background:var(--orange);border-radius:3px;text-decoration:none}
.btn-nav{font-size:11.5px;padding:8px 11px;margin-left:0}

/* hero */
.hero{position:relative;height:365px;text-align:center;color:var(--white)}
.hero-art{position:absolute;inset:0;background:radial-gradient(circle at 85% 10%,#2a63f0 0,transparent 40%),radial-gradient(circle at 95% 90%,#1d56e8 0,transparent 35%),linear-gradient(135deg,#0b36b8 0%,#0c3fcf 50%,#1046d6 100%)}
.hero-content{position:relative;padding-top:92px}
.hero h1{font-size:35px;line-height:39px;font-weight:700;letter-spacing:-.2px}
.hero p{font-size:15px;line-height:25px;margin-top:9px}
.btn-hero{font-size:13.5px;padding:10px 13px;margin-top:14px}

/* overview */
.overview{height:341px;background:var(--blue);color:var(--white);text-align:center;padding-top:72px}
.section-title{font-size:35px;font-weight:800;letter-spacing:.3px;line-height:40px}
.overview p{font-size:15px;line-height:20px;width:700px;margin:34px auto 0}
.btn-outline{display:inline-block;margin-top:16px;border:1px solid var(--white);border-radius:3px;padding:6px 10px;font-size:14px;font-weight:700;color:var(--white);text-decoration:none}

/* solutions */
.solutions{height:477px;background:var(--soft);text-align:center;padding-top:82px}
.cards{display:flex;gap:26px;justify-content:center;margin-top:52px}
.card{width:262px;height:223px;background:var(--white);border-radius:6px;box-shadow:0 2px 10px rgba(20,40,90,.08);padding:30px 14px 0}
.icon-ring{width:55px;height:55px;margin:0 auto;border:1.3px solid var(--blue);border-radius:50%;display:flex;align-items:center;justify-content:center}
.card h3{font-size:15.5px;font-weight:600;margin-top:14px}
.card p{font-size:11.5px;line-height:16.5px;color:var(--muted);margin-top:6px}
.learn{display:inline-block;margin-top:8px;font-size:11.5px;font-weight:600;color:var(--orange);text-decoration:none}

/* characteristics */
.characteristics{height:391px;padding-top:65px;text-align:center}
.char-grid{position:relative;width:836px;margin:46px auto 0;display:grid;grid-template-columns:1fr 1fr;text-align:left}
.char-grid::before{content:"";position:absolute;left:418px;top:0;bottom:0;width:1px;background:var(--line)}
.char{display:flex;gap:12px;align-items:flex-start;height:103px;padding-top:6px}
.char:nth-child(odd){padding-right:30px}
.char:nth-child(even){padding-left:42px}
.char:nth-child(-n+2){border-bottom:1px solid var(--line)}
.char:nth-child(n+3){padding-top:13px}
.char .icon-ring{width:61px;height:61px;flex:none;margin:0}
.char h4{font-size:15.5px;font-weight:600;margin-top:6px}
.char p{font-size:11.5px;line-height:16px;color:var(--muted);margin-top:4px}

/* cta */
.cta{height:285px;background:var(--orange);text-align:center;padding-top:80px}
.btn-cta{background:var(--blue);font-size:19px;padding:13px 18px;margin-top:30px;border-radius:2px}

/* footer */
.site-footer{height:189px;background:var(--footer);color:var(--white);position:relative}
.footer-cols{display:flex;padding:31px 0 0 158px}
.footer-col{width:179px}
.footer-col h5{font-size:10px;font-weight:600;margin-bottom:10px}
.footer-col li{list-style:none;font-size:8.5px;line-height:18px;color:#d9d9d9}
.copyright{position:absolute;left:0;right:0;bottom:31px;text-align:center;font-size:7.5px;color:#bdbdbd}
</style>
</head>
<body>
<div class="page">
  <header class="site-header">
    <div class="brand"><span class="brand-dot"></span>QV HOLDINGS</div>
    <nav class="main-nav">
      <span>Home</span><span>Platform</span><span>Solutions</span><span>Insights</span><span>Company</span><span>Contact</span>
      <a class="btn btn-nav" href="#">Request a Technical Walkthrough</a>
    </nav>
  </header>

  <section class="hero">
    <div class="hero-art" role="img" aria-label="Abstract deep blue background with network lines and nodes"></div>
    <div class="hero-content">
      <h1>Actuarial software for structured,<br>auditable financial analysis</h1>
      <p>Software that translates actuarial methodologies into disciplined<br>decision-ready analytical tools across diverse regulatory environments.</p>
      <a class="btn btn-hero" href="#">Request a Technical Walkthrough</a>
    </div>
  </section>

  <section class="overview">
    <h2 class="section-title">PLATFORM OVERVIEW</h2>
    <p>QV Holdings develops modular actuarial software designed to support reserving, valuation, pricing and enterprise risk management workflows across diverse regulatory environments. Our platform translates established actuarial methodologies into disciplined, audit-ready tools, ensuring transparency and governance at every step.</p>
    <a class="btn-outline" href="#">EXPLORE PLATFORM</a>
  </section>

  <section class="solutions">
    <h2 class="section-title">CORE SOLUTIONS</h2>
    <div class="cards">
      <article class="card">
        <div class="icon-ring"><svg width="30" height="30" viewBox="0 0 30 30" fill="none" stroke="#0052ff" stroke-width="1.4"><rect x="3" y="4" width="24" height="16" rx="1"/><path d="M15 20v5M9 26h12M7 8h6M7 12h6M7 16h6M17 8h6M17 12h6"/></svg></div>
        <h3>Reserving &amp; Valuation</h3>
        <p>Structured workflows and financial reporting across jurisdictions built on disciplined actuarial methodologies.</p>
        <a class="learn" href="#">Learn more →</a>
      </article>
      <article class="card">
        <div class="icon-ring"><svg width="30" height="30" viewBox="0 0 30 30" fill="none" stroke="#0052ff" stroke-width="1.4"><circle cx="15" cy="15" r="7"/><path d="M20 20l6 6M15 11v8M13 13h3.5a1.5 1.5 0 010 3h-3a1.5 1.5 0 000 3H17"/></svg></div>
        <h3>Pricing</h3>
        <p>Insurance and reinsurance pricing models grounded in transparency, enabling accurate, explainable decisions.</p>
        <a class="learn" href="#">Learn more →</a>
      </article>
      <article class="card">
        <div class="icon-ring"><svg width="30" height="30" viewBox="0 0 30 30" fill="none" stroke="#0052ff" stroke-width="1.4"><rect x="5" y="10" width="10" height="15"/><path d="M8 14h4M8 18h4M8 22h4M19 25V8M16 11l3-4 3 4"/><circle cx="22" cy="21" r="3"/></svg></div>
        <h3>Enterprise Risk Management</h3>
        <p>Tools supporting reinsurance optimization and capital modeling for comprehensive enterprise risk management.</p>
        <a class="learn" href="#">Learn more →</a>
      </article>
    </div>
  </section>

  <section class="characteristics">
    <h2 class="section-title">PLATFORM CHARACTERISTICS</h2>
    <div class="char-grid">
      <div class="char">
        <div class="icon-ring"><svg width="30" height="30" viewBox="0 0 30 30" fill="none" stroke="#0052ff" stroke-width="1.4"><rect x="3" y="5" width="5" height="4"/><rect x="3" y="21" width="5" height="4"/><circle cx="15" cy="7" r="2"/><circle cx="15" cy="15" r="2"/><path d="M8 7h5M17 7h9M5 15h8M17 15h9M8 23h18"/></svg></div>
        <div><h4>Structured Workflows</h4><p>Disciplined processes built to support multi-jurisdictional review and actuarial governance.</p></div>
      </div>
      <div class="char">
        <div class="icon-ring"><svg width="30" height="30" viewBox="0 0 30 30" fill="none" stroke="#0052ff" stroke-width="1.4"><circle cx="15" cy="13" r="8"/><circle cx="15" cy="13" r="3"/><path d="M11 21v5M19 21v5"/></svg></div>
        <div><h4>Transparent Assumptions</h4><p>Clear documentation of assumptions and methodologies for auditability and defensibility.</p></div>
      </div>
      <div class="char">
        <div class="icon-ring"><svg width="30" height="30" viewBox="0 0 30 30" fill="none" stroke="#0052ff" stroke-width="1.4"><path d="M7 4h11l5 5v17H7z"/><path d="M18 4v5h5M10 13h10M10 17h10M10 21h7"/></svg></div>
        <div><h4>Comparative Analysis</h4><p>Capabilities for scenario comparison and sensitivity analysis to inform professional judgment.</p></div>
      </div>
      <div class="char">
        <div class="icon-ring"><svg width="30" height="30" viewBox="0 0 30 30" fill="none" stroke="#0052ff" stroke-width="1.4"><circle cx="15" cy="11" r="6"/><path d="M12 11l2 2 4-4M4 20c4 0 6 5 11 5s7-5 11-5"/></svg></div>
        <div><h4>Governance Ready</h4><p>Outputs designed to support regulator and board review, ensuring compliance and clarity.</p></div>
      </div>
    </div>
  </section>

  <section class="cta">
    <h2 class="section-title">INTERESTED IN EXPLORING THE PLATFORM?</h2>
    <a class="btn btn-cta" href="#">Request a Technical Walkthrough</a>
  </section>

  <footer class="site-footer">
    <div class="footer-cols">
      <div class="footer-col"><h5>Company</h5><ul><li>About</li><li>Careers</li><li>Legal</li></ul></div>
      <div class="footer-col"><h5>Platform</h5><ul><li>Overview</li><li>Reserving &amp; Valuation</li><li>Pricing</li><li>Enterprise Risk Management</li></ul></div>
      <div class="footer-col"><h5>Insights</h5><ul><li>Articles</li><li>Guides</li><li>News</li></ul></div>
      <div class="footer-col"><h5>Contact</h5><ul><li>Email Us</li><li>Request a Walkthrough</li></ul></div>
    </div>
    <p class="copyright">© 2026 QV Holdings. All rights reserved.</p>
  </footer>
</div>
</body>
</html>
```